Marco Bellin Photography needs a business card designs

I am looking for a business card with a logo clean and simple which I can use that logo on my website or on my pictures. It has to be very classy and very professional. Please look at my website at www.marcobphoto.com for my signature. I'm thinking of something like that for my signature/logo. I'm still working on my website but you get an idea. I'm open to any design but not too busy graphics.

I will be printing the business card from kelvaprint.com.

Surprise me :)

contact me if you have any questions.

-MB
Updates

I'm receiving a lot of black background at the moment. I know my website is all black doesn't mean I want my card to be all black. Please send in with some white background as well. Thanks :)

check out some business cards that I found online. I think they are simple and look really awesome. I don't want a card that is too busy.

http://www.marcobphoto.com/p270092084

Reason: Please extend the date for me. I haven't really receive any good design yet.

Industry/Entity Type

Printing

Requirements
Nice to have
• -a logo that related to my first and last initial of my name "MB"
-double sided
Should not have
• -I don't want my background to be all black.
-no pictures on the card

```html
<!DOCTYPE html>
<html lang="en">
<head>
<meta charset="utf-8">
<title>Marco Bellin Photography – Business Card</title>
<link rel="stylesheet" href="https://fonts.googleapis.com/css2?family=Jost:wght@400&display=swap">
<style>
  :root {
    --page: #ffffff;
    --card-white: #ffffff;
    --card-black: #000000;
    --brand-red: #e8192c;
    --ink: #1a1a1a;
    --label-grey: #555555;
    --mark-faint: #f0f0f0;
    --band-glow: #6a6a6a;
  }
  html, body {
    margin: 0;
    padding: 0;
    width: 1200px;
    height: 861px;
    overflow: hidden;
    background: var(--page);
    font-family: "Jost", "Futura", sans-serif;
  }
  .canvas {
    position: relative;
    width: 1200px;
    height: 861px;
  }
  .card {
    position: absolute;
    top: 83px;
    width: 459px;
    height: 700px;
    overflow: hidden;
    box-shadow: 4px 6px 14px rgba(0, 0, 0, 0.22);
  }
  .card--front { left: 83px; background: var(--card-white); }
  .card--back { left: 642px; background: var(--card-black); }

  .front__mark {
    position: absolute;
    left: 14px;
    top: 30px;
    margin: 0;
    font-size: 280px;
    line-height: 1;
    color: var(--mark-faint);
    letter-spacing: -6px;
    white-space: nowrap;
  }
  .front__name {
    position: absolute;
    left: 27px;
    top: 359px;
    margin: 0;
    font-size: 62px;
    font-weight: 400;
    line-height: 1;
    color: var(--brand-red);
    white-space: nowrap;
  }
  .front__role {
    position: absolute;
    left: 29px;
    top: 414px;
    margin: 0;
    font-size: 28px;
    line-height: 1;
    letter-spacing: 9.5px;
    color: var(--ink);
    white-space: nowrap;
  }
  .contact {
    position: absolute;
    left: 27px;
    top: 483px;
    margin: 0;
    font-size: 21px;
    line-height: 31px;
  }
  .contact__row { display: flex; white-space: nowrap; }
  .contact__label { width: 84px; color: var(--label-grey); }
  .contact__value { color: var(--ink); }
  .front__band {
    position: absolute;
    left: 0;
    bottom: 0;
    width: 100%;
    height: 83px;
    background: radial-gradient(ellipse 45% 120% at 50% 0%, var(--band-glow), var(--card-black));
  }
  .front__url {
    position: absolute;
    left: 27px;
    top: 19px;
    margin: 0;
    font-size: 39px;
    line-height: 1;
    color: var(--card-white);
    white-space: nowrap;
  }

  .back__mark {
    position: absolute;
    left: 0;
    width: 100%;
    top: 175px;
    margin: 0;
    text-align: center;
    font-size: 210px;
    line-height: 1;
    color: var(--card-white);
  }
  .back__name {
    position: absolute;
    left: 24px;
    top: 437px;
    margin: 0;
    font-size: 80px;
    font-weight: 400;
    line-height: 1;
    color: var(--brand-red);
    white-space: nowrap;
  }
  .back__tagline {
    position: absolute;
    left: 26px;
    top: 506px;
    margin: 0;
    font-size: 33px;
    line-height: 1;
    letter-spacing: 14.5px;
    color: var(--card-white);
    white-space: nowrap;
  }
</style>
</head>
<body>
<main class="canvas">
  <section class="card card--front" aria-label="Card front">
    <p class="front__mark" aria-hidden="true">MB</p>
    <h1 class="front__name">Marco Bellin</h1>
    <p class="front__role">PHOTOGRAPHER</p>
    <div class="contact">
      <div class="contact__row"><span class="contact__label">Phone:</span><span class="contact__value">555-01928</span></div>
      <div class="contact__row"><span class="contact__label">E-mail:</span><span class="contact__value">info@marcobphoto.com</span></div>
    </div>
    <div class="front__band">
      <p class="front__url">www.marcobphoto.com</p>
    </div>
  </section>

  <section class="card card--back" aria-label="Card back">
    <p class="back__mark">MB</p>
    <h2 class="back__name">Marco Bellin</h2>
    <p class="back__tagline">PHOTOGRAPHY</p>
  </section>
</main>
</body>
</html>
```